Makers' Hollow - Landing page for small and large screen

Makers’ Hollow gives you the space you need to take your side project from idea to reality.

With three days of focused work, it’s a place for you iron out the details of your business idea away from the distractions of the city.

The full copy and structure is here:
https://www.makershollow-example.co.uk/landing

What it needs, a touch of colour.

Target Market(s)

25-35 working in digital industry, software developer, a UI or UX designer

Number of Pages Required

1 page

Font styles to use
Sans Serif

Colors
0292cd
33b8a4
86cfc6
fdf9cf
ec1f27

Requirements
Should not have
• gradients or too much images

```html
<!DOCTYPE html>
<html lang="en">
<head>
<meta charset="utf-8">
<title>Makers’ Hollow — Landing</title>
<link href="https://fonts.googleapis.com/css2?family=Poppins:wght@500;600;700&family=Open+Sans:wght@400;600;700&display=swap" rel="stylesheet">
<style>
:root{
  --blue:#0292cd;
  --teal:#33b8a4;
  --mint:#86cfc6;
  --cream:#fdf9cf;
  --red:#ec1f27;
  --ink:#1d1d1d;
  --text:#555;
  --grey-bg:#f1f1f1;
  --line:#d9d9d9;
  --dark:#2b2b2b;
  --white:#fff;
}
*{box-sizing:border-box;margin:0;padding:0}
html,body{width:1200px;height:3912px;overflow:hidden}
body{font-family:"Open Sans",Arial,sans-serif;color:var(--text);background:var(--white);position:relative}
section,header,footer{position:absolute;left:0;width:1200px;overflow:hidden}
h1,h2,h3,.brand-name{font-family:"Poppins",Arial,sans-serif}

/* hero */
.hero{top:0;height:600px}
.hero-photo{position:absolute;inset:0;background:linear-gradient(160deg,#5f6366 0%,#3d4144 45%,#24272a 100%)}
.hero-shade{position:absolute;inset:0;background:rgba(0,0,0,.35)}
.brand{position:absolute;left:40px;top:16px;color:var(--white)}
.brand-name{font-size:34px;font-weight:700;line-height:1.1}
.brand-tag{font-size:17px;letter-spacing:1.5px}
.main-nav{position:absolute;right:40px;top:18px;display:flex;gap:26px}
.main-nav a{color:var(--white);font-size:13px;font-weight:700;text-decoration:none;letter-spacing:.5px}
.hero-title{position:absolute;left:220px;top:455px;color:var(--white)}
.hero-title .pre{font-size:28px;font-weight:600}
.hero-title h1{font-size:48px;font-weight:700;line-height:1.1}

/* feature blocks */
.feature-one{top:600px;height:540px;background:var(--grey-bg)}
.feature-two{top:1140px;height:540px;background:var(--white)}
.feature-copy{position:absolute}
.feature-copy h2{color:var(--ink);font-size:21px;font-weight:700;text-transform:uppercase;line-height:1.4;margin-bottom:24px}
.feature-copy p{font-size:15px;line-height:1.6;margin-bottom:18px}
.feature-one .feature-copy{left:140px;top:95px;width:530px}
.feature-two .feature-copy{left:548px;top:85px;width:520px}
.feature-art{position:absolute;width:340px;height:340px;border-radius:50%;background:var(--white);box-shadow:0 2px 12px rgba(0,0,0,.12);display:flex;align-items:center;justify-content:center}
.feature-art span{display:block;width:270px;height:270px;border-radius:50%;background:var(--teal)}
.feature-one .feature-art{left:760px;top:80px}
.feature-two .feature-art{left:135px;top:80px}

/* benefits */
.benefits{top:1680px;height:620px;background:var(--white)}
.benefits h2{position:absolute;top:55px;width:100%;text-align:center;color:var(--ink);font-size:26px;font-weight:700;text-transform:uppercase}
.benefits svg.rays{position:absolute;inset:0}
.hub{position:absolute;left:480px;top:240px;width:240px;height:240px;border-radius:50%;background:var(--white);box-shadow:0 0 0 14px #f3f3f3;display:flex;flex-direction:column;align-items:center;justify-content:center;text-align:center}
.hub strong{font-family:"Poppins",sans-serif;font-size:36px;line-height:1.05;color:var(--ink)}
.hub small{font-size:14px;margin-top:10px;letter-spacing:1px}
.perk{position:absolute;display:flex;align-items:center;gap:14px;font-size:14px;line-height:1.45;color:#444}
.perk .icon{flex:none;width:58px;height:58px;border-radius:50%;background:var(--blue);display:flex;align-items:center;justify-content:center}
.perk.left{flex-direction:row-reverse;text-align:right}
.perk.top{flex-direction:column;text-align:center;width:260px;gap:8px}

/* stay */
.stay{top:2300px;height:300px;background:linear-gradient(90deg,#23907f,#33b8a4 50%,#2a9d8b);color:var(--white);text-align:center}
.stay-photo{position:absolute;inset:0;background:rgba(20,80,70,.25)}
.stay h2{position:relative;margin-top:62px;font-size:30px;font-weight:700;text-transform:uppercase}
.stay p{position:relative;width:640px;margin:18px auto 0;font-size:15px;font-weight:600;line-height:1.6}

/* organisers */
.organisers{top:2600px;height:720px;background:var(--white)}
.organisers h2{position:absolute;top:65px;width:100%;text-align:center;color:var(--ink);font-size:26px;font-weight:700;text-transform:uppercase}
.organiser{position:absolute;top:200px;width:440px;height:460px;border:1px solid var(--line);text-align:center;padding:110px 40px 0}
.organiser.first{left:145px}
.organiser.second{left:615px}
.avatar{position:absolute;left:155px;top:-60px;width:130px;height:130px;border-radius:50%;border:6px solid var(--white);box-shadow:0 1px 8px rgba(0,0,0,.2)}
.organiser.first .avatar{background:#5a4e46}
.organiser.second .avatar{background:#8a6a55}
.organiser h3{color:var(--ink);font-size:22px;font-weight:600;margin-bottom:18px}
.organiser p{font-size:14px;line-height:1.6}
.socials{display:flex;gap:12px;justify-content:center;margin-top:28px}
.socials i{width:28px;height:28px;border-radius:50%;display:block}
.socials i:nth-child(1){background:#f2c300}
.socials i:nth-child(2){background:#222}
.socials i:nth-child(3){background:var(--blue)}

/* feedback */
.feedback{top:3320px;height:440px;background:var(--blue);color:var(--white);text-align:center}
.feedback h2{margin-top:95px;font-size:32px;font-weight:700;text-transform:uppercase}
.feedback p{width:620px;margin:24px auto 0;font-size:16px;line-height:1.6}
.btn{display:inline-block;margin-top:40px;background:var(--teal);color:var(--white);font-weight:700;font-size:15px;padding:18px 36px;letter-spacing:.5px;text-decoration:none;text-transform:uppercase}

/* footer */
.site-footer{top:3760px;height:152px;background:var(--dark);color:var(--white)}
.site-footer .brand{top:38px;left:40px}
.footer-nav{position:absolute;right:40px;top:55px;display:flex;gap:18px}
.footer-nav a{color:var(--white);font-size:12px;font-weight:700;text-decoration:none}
.copyright{position:absolute;right:40px;top:85px;font-size:11px;color:#bbb}
</style>
</head>
<body>

<header class="hero">
  <div class="hero-photo" role="img" aria-label="Photo of a bright open-plan workspace with desks and large windows"></div>
  <div class="hero-shade"></div>
  <div class="brand"><div class="brand-name">Makers’ Hollow</div><div class="brand-tag">build. share. grow together</div></div>
  <nav class="main-nav"><a href="#">HOME</a><a href="#">ABOUT US</a><a href="#">SERVICES</a><a href="#">CONTACT US</a></nav>
  <div class="hero-title"><div class="pre">Welcome to</div><h1>MAKERS’ HOLLOW</h1></div>
</header>

<section class="feature-one">
  <div class="feature-copy">
    <h2>Makers’ Hollow gives you the space you need to take your side project from idea to reality.</h2>
    <p>Calling all creatives! Whether you’re a software developer, a UI or UX designer, a product creator or an artworker, you’ll know only too well that great work rarely materialises when you’re in the wrong environment.</p>
    <p>Phones buzzing. Emails pinging. Video calls incoming. Distractions are everywhere – and they do nothing for your motivation.</p>
    <p>So, if you have a seed of a business idea and need to reclaim some focus, Makers’ Hollow is for you. Or maybe you’ve created a product, sought a patent and you’re ready – and raring – to go.</p>
  </div>
  <div class="feature-art"><span role="img" aria-label="Illustration of a developer at work"></span></div>
</section>

<section class="feature-two">
  <div class="feature-art"><span role="img" aria-label="Illustration of a glowing light bulb"></span></div>
  <div class="feature-copy">
    <h2>With three days of focused work, it’s a place for you iron out the details of your business idea away from the distractions of the city.</h2>
    <p>Whatever stage your side hustle’s at, we’re here to help it thrive. Our warm and friendly retreat is just that: a place to create, connect and collaborate with likeminded folks. Oh, and there’s yoga, meditation, healthy meals and snacks, and all the feedback you need to power on through.</p>
    <p>And while you’re busy getting your side project off the ground, we’ll cook up three healthy meals each day so that you don’t have to worry about cooking. We’ll even make sure you have a steady supply of healthy low-sugar snacks to help fuel all those bright ideas.</p>
  </div>
</section>

<section class="benefits">
  <h2>Join the retreat and enjoy</h2>
  <svg class="rays" width="1200" height="620" aria-hidden="true">
    <g stroke="#e2e2e2" stroke-width="1.5">
      <line x1="600" y1="360" x2="600" y2="230"/>
      <line x1="600" y1="360" x2="300" y2="280"/>
      <line x1="600" y1="360" x2="290" y2="375"/>
      <line x1="600" y1="360" x2="370" y2="480"/>
      <line x1="600" y1="360" x2="900" y2="280"/>
      <line x1="600" y1="360" x2="910" y2="375"/>
      <line x1="600" y1="360" x2="830" y2="480"/>
    </g>
  </svg>
  <div class="hub"><strong>MAKERS’<br>HOLLOW</strong><small>build. share. grow together</small></div>

  <div class="perk top" style="left:470px;top:112px">
    <div class="icon"><svg width="30" height="30" viewBox="0 0 30 30"><path d="M4 6h22v13H12l-6 5v-5H4z" fill="#fff"/></svg></div>
    <div>Good, honest feedback and insight from fellow attendees</div>
  </div>

  <div class="perk left" style="left:40px;top:251px;width:290px">
    <div class="icon"><svg width="30" height="30" viewBox="0 0 30 30"><path d="M3 16l6-6 6 4 6-4 6 6-9 7z" fill="#fff"/></svg></div>
    <div>The opportunity to collaborate with likeminded creatives</div>
  </div>
  <div class="perk left" style="left:20px;top:346px;width:300px">
    <div class="icon"><svg width="30" height="30" viewBox="0 0 30 30"><rect x="7" y="4" width="16" height="22" rx="1" fill="#fff"/><rect x="11" y="9" width="8" height="2" fill="#0292cd"/><rect x="11" y="14" width="8" height="2" fill="#0292cd"/></svg></div>
    <div>A chance to hone your side project away from the office</div>
  </div>
  <div class="perk left" style="left:110px;top:451px;width:290px">
    <div class="icon"><svg width="30" height="30" viewBox="0 0 30 30"><rect x="5" y="7" width="20" height="18" rx="2" fill="#fff"/><rect x="5" y="7" width="20" height="5" fill="#cfeefa"/></svg></div>
    <div>Three full days of distraction-free work</div>
  </div>

  <div class="perk" style="left:870px;top:251px;width:290px">
    <div class="icon"><svg width="30" height="30" viewBox="0 0 30 30"><circle cx="15" cy="7" r="3.5" fill="#fff"/><path d="M5 22l10-9 10 9z" fill="#fff"/></svg></div>
    <div>Daily yoga and meditation to help fuel your ideas</div>
  </div>
  <div class="perk" style="left:880px;top:346px;width:300px">
    <div class="icon"><svg width="30" height="30" viewBox="0 0 30 30"><circle cx="15" cy="16" r="9" fill="#fff"/><path d="M15 7c1-3 4-4 6-3-1 3-4 4-6 3z" fill="#cfeefa"/></svg></div>
    <div>Healthy low-sugar snacks to get you through the day</div>
  </div>
  <div class="perk" style="left:800px;top:451px;width:290px">
    <div class="icon"><svg width="30" height="30" viewBox="0 0 30 30"><circle cx="15" cy="15" r="9" fill="none" stroke="#fff" stroke-width="2.5"/><line x1="4" y1="5" x2="4" y2="25" stroke="#fff" stroke-width="2"/><line x1="26" y1="5" x2="26" y2="25" stroke="#fff" stroke-width="2"/></svg></div>
    <div>Three, nutritious and delicious meals a day</div>
  </div>
</section>

<section class="stay">
  <div class="stay-photo" role="img" aria-label="Photo of the retreat venue in a calm countryside setting, tinted teal"></div>
  <h2>Where you’ll be staying</h2>
  <p>A retreat wouldn’t be a retreat without a calm, peaceful and picturesque location. It’s the reason we’re working hard behind the scenes to find the ideal spot to host you. Of course, it’ll have Wi-Fi (4G internet – but it’ll also be somewhere that will allow for maximum creativity.</p>
</section>

<section class="organisers">
  <h2>Meet your retreat organisers</h2>
  <article class="organiser first">
    <div class="avatar" role="img" aria-label="Portrait photo of Tomas Verel"></div>
    <h3>Tomas Verel</h3>
    <p>A software engineer in London, Tomas knows only too well the challenges faced by creatives. On the nature side he’s organised Makers’ Hollow to give everyone the space and time to do their best work. Armed with his trusty camera, photographer Tomas is also a computer enthusiast and a thoroughly good egg.</p>
    <div class="socials"><i></i><i></i><i></i></div>
  </article>
  <article class="organiser second">
    <div class="avatar" role="img" aria-label="Portrait photo of Lina Marsh"></div>
    <h3>Lina Marsh</h3>
    <p>An internationally certified yoga teacher, Lina loves connecting with people and discovering how she can help them get the most out of their day – and their work. Giving attendees the time to enjoy some self care in the form of a gentle yoga session is what drives her. Help you unleash those ideas!</p>
    <div class="socials"><i></i><i></i><i></i></div>
  </article>
</section>

<section class="feedback">
  <h2>What do you think?</h2>
  <p>Sound good? Keen to know more? Share some feedback via the button below and we can hone the retreat to suit you.</p>
  <a class="btn" href="#">Share your thoughts</a>
</section>

<footer class="site-footer">
  <div class="brand"><div class="brand-name">Makers’ Hollow</div><div class="brand-tag">build. share. grow together</div></div>
  <nav class="footer-nav"><a href="#">HOME</a><a href="#">ABOUT US</a><a href="#">SERVICES</a><a href="#">CONTACT US</a></nav>
  <div class="copyright">Copyright © 2016 All Rights Reserved</div>
</footer>

</body>
</html>
```